Business Card Design Project

A double sided business card for presentation to business leaders in corporate.

Target Market(s)

Corporate, business professionals, HR

Industry/Entity Type

Business

Requirements
Must have
• FRONT

Logo

www.brightlanecoaching.com.au

BACK

Mara Pollen-Drew
Director

+ 61 (0) 418 536 204
mara@brightlanecoaching.com.au
www.brightlanecoaching.com.au

Growth through energy and employee engagement

("ripples" of logo, bottom corner)

Must be:
- double sided
size: 86 x 54mm
supplied as one pdf with crop marks shown (+- 1mm, with 2-3 mm bleed)

```html
<!DOCTYPE html>
<html lang="en">
<head>
<meta charset="utf-8">
<title>Bright Lane Coaching – Business Card</title>
<link rel="stylesheet" href="https://fonts.googleapis.com/css2?family=Roboto+Condensed:wght@400&display=swap">
<style>
  :root {
    --purple: #6b0f8f;
    --charcoal: #3d4547;
    --ink: #1a1a1a;
    --paper: #ffffff;
    --type: "Roboto Condensed", Arial Narrow, sans-serif;
  }
  * { box-sizing: border-box; margin: 0; padding: 0; }
  html, body { width: 1200px; height: 902px; overflow: hidden; background: var(--paper); }
  .board {
    position: relative; width: 1200px; height: 902px;
    border: 2px solid var(--ink); font-family: var(--type);
  }
  .card {
    position: absolute; left: 343px; width: 514px; height: 324px;
    border: 1.5px solid var(--ink); border-radius: 16px;
    overflow: hidden; background: var(--paper);
  }
  .card--front { top: 100px; }
  .card--back { top: 477px; }

  .band { position: absolute; left: 0; right: 0; height: 28px; }
  .band--top { top: 0; background: var(--purple); }
  .band--bottom { bottom: 0; background: var(--charcoal); }

  .brand { position: absolute; display: flex; align-items: center; gap: 10px; color: var(--purple); }
  .brand__dot { flex: none; border-radius: 50%; background: var(--purple); }
  .brand__name { line-height: 1.05; font-weight: 400; }
  .card--front .brand { left: 50px; top: 122px; }
  .card--front .brand__dot { width: 22px; height: 22px; }
  .card--front .brand__name { font-size: 24px; }
  .card--back .brand { right: 36px; top: 176px; }
  .card--back .brand__dot { width: 28px; height: 28px; }
  .card--back .brand__name { font-size: 30px; }

  .front-url {
    position: absolute; right: 40px; top: 144px;
    font-size: 18px; color: var(--purple);
  }
  .tagline {
    position: absolute; right: 36px; top: 36px; text-align: right;
    font-size: 20px; line-height: 27px; color: var(--purple);
  }
  .person { position: absolute; left: 44px; top: 131px; color: var(--charcoal); }
  .person__name { font-size: 19px; letter-spacing: 2.4px; }
  .person__role { font-size: 11.5px; letter-spacing: 2px; margin-top: 4px; }
  .contact {
    position: absolute; left: 44px; top: 215px; list-style: none;
    font-size: 13px; line-height: 25.5px; color: var(--charcoal);
  }
</style>
</head>
<body>
<div class="board">
  <section class="card card--front" aria-label="Card front">
    <div class="band band--top"></div>
    <div class="brand">
      <span class="brand__dot"></span>
      <span class="brand__name">Bright Lane<br>Coaching</span>
    </div>
    <p class="front-url">www.brightlanecoaching.com.au</p>
    <div class="band band--bottom"></div>
  </section>

  <section class="card card--back" aria-label="Card back">
    <p class="tagline">Growth through energy and<br>employee engagement</p>
    <div class="person">
      <p class="person__name">Mara Pollen-Drew</p>
      <p class="person__role">director</p>
    </div>
    <ul class="contact">
      <li>+ 61 (0) 418 536 204</li>
      <li>mara@brightlanecoaching.com.au</li>
      <li>www.brightlanecoaching.com.au</li>
    </ul>
    <div class="brand">
      <span class="brand__dot"></span>
      <span class="brand__name">Bright Lane<br>Coaching</span>
    </div>
  </section>
</div>
</body>
</html>
```